Redesign and move to Wordpress for quarvendo.com

Our website needs a redesign and at the same time we are moving it to Wordpress. Please help us with a new digital professional look and feel.

We are an Australian Software Engineering company specialising in advanced software development using in A.I., PLatform Engineering, Integration and Cloud. See the current quarvendo.com for more information about us.

```html
<!DOCTYPE html>
<html lang="en">
<head>
<meta charset="utf-8">
<title>quarvendo — Reliable. Smart. Custom. Software</title>
<link rel="stylesheet" href="https://fonts.googleapis.com/css2?family=Space+Grotesk:wght@400;500;700&family=Space+Mono:wght@700&display=swap">
<style>
:root{
  --page:#f2f2f2;
  --brand-blue:#1564a3;
  --teal:#4fc3bc;
  --ink:#111111;
  --text:#2b2b2b;
  --client:#3a3a3a;
  --white:#ffffff;
  --hero:#f5f5f5;
}
*{box-sizing:border-box;margin:0;padding:0}
html,body{width:1200px;height:900px;overflow:hidden}
body{background:var(--page);font-family:"Space Grotesk",sans-serif;color:var(--ink);position:relative}
.site{position:absolute;left:68px;top:90px;width:1064px;height:810px;background:var(--hero);overflow:hidden}
.header{position:absolute;left:0;top:0;width:100%;height:73px;background:var(--brand-blue)}
.brand{position:absolute;left:17px;top:19px;display:flex;align-items:center;gap:12px;color:var(--white);font-size:25px;font-weight:400;letter-spacing:1px}
.brand-mark{width:30px;height:30px;border:3px solid var(--white)}
.nav{position:absolute;left:365px;top:27px;display:flex;gap:33px;color:var(--white);font-size:16px;font-weight:500}
.nav a{color:inherit;text-decoration:none}
.cta{position:absolute;left:866px;top:10px;width:181px;height:51px;background:var(--white);color:var(--brand-blue);font-size:18.5px;font-weight:700;display:flex;align-items:center;justify-content:center}
.hero-title{position:absolute;left:0;top:130px;width:100%;text-align:center;font-size:54px;font-weight:700;line-height:66px;letter-spacing:-0.5px}
.accent{background:linear-gradient(180deg,#3aa6c9,#1d6fa8);-webkit-background-clip:text;background-clip:text;color:transparent}
.hero-lede{position:absolute;left:0;top:271px;width:100%;text-align:center;font-size:16px;line-height:20px;color:var(--text)}
.band{position:absolute;left:0;top:556px;width:100%;height:153px;background:var(--brand-blue)}
.clients{position:absolute;left:0;top:709px;width:100%;height:101px;background:var(--white)}
.client{position:absolute;top:42px;transform:translateX(-50%);font-size:34px;font-weight:700;color:var(--client);letter-spacing:-1px;white-space:nowrap}
.card{position:absolute;top:407px;width:220px;height:197px;border:6px solid var(--teal);text-align:center}
.card-title{margin-top:28px;font-family:"Space Mono",monospace;font-size:22px;font-weight:700;line-height:26px;color:var(--ink)}
.card-text{margin:9px auto 0;width:152px;font-size:11px;line-height:13.5px;color:var(--text)}
.card-btn{position:absolute;left:27px;top:122px;width:154px;height:36px;background:var(--teal);color:var(--white);font-size:16px;font-weight:700;display:flex;align-items:center;justify-content:center}
</style>
</head>
<body>
<div class="site">
  <header class="header">
    <div class="brand"><span class="brand-mark"></span>quarvendo</div>
    <nav class="nav"><a href="#">Services</a><a href="#">About</a><a href="#">Use Cases</a><a href="#">Contact</a></nav>
    <a class="cta">Talk To Our CTO</a>
  </header>

  <h1 class="hero-title">Reliable. Smart. Custom.<br>S<span class="accent">o</span>ftware</h1>
  <p class="hero-lede">Building software solutions tailored to your business needs.<br>From legacy system enablement to advanced AI systems</p>

  <div class="band"></div>

  <section class="card" style="left:169px">
    <h2 class="card-title">AI</h2>
    <p class="card-text">Intelligent automation &amp; conversational systems tailored for your needs.</p>
    <a class="card-btn">Explore AI</a>
  </section>
  <section class="card" style="left:422px">
    <h2 class="card-title">PLatform</h2>
    <p class="card-text">Reliable, unified &amp; scalable integration for legacy and modern systems.</p>
    <a class="card-btn">Explore IPAAS</a>
  </section>
  <section class="card" style="left:676px">
    <h2 class="card-title">Cloud</h2>
    <p class="card-text">Secure, optimized &amp; robust cloud infrastructure for your workflow.</p>
    <a class="card-btn">Explore Cloud</a>
  </section>

  <div class="clients">
    <div class="client" style="left:173px">Corvale</div>
    <div class="client" style="left:446px">Haldane</div>
    <div class="client" style="left:695px">Nexaro</div>
    <div class="client" style="left:892px">Trakway</div>
  </div>
</div>
</body>
</html>
```